Psychology Practice in Sydney Website Redesign

Corlew Psychology is a Psychology Practice with locations in Westmead, Chatswood and the CBD. They have specialties in treating children, and in treating eating disorders. They also treat anxiety and depression. They have ~10-20 clinical psychologists working for them.

The client wants the site to be modern and professional, he said:
”Mainly gonna be the credibility, people already know of us, but some could find us on google search, site needs to be a bit sexy.”

The client prefers websites with a heavy use of negative space and a largely minimal, modern design. (e.g. https://harbourlanemind-example.com.au/, https://www.fenmora-example.net.au/, https://tovalin-example.com.au/). He wants the site to be approachable without being unprofessional, and to be modern without being clinical. This is their current site: https://www.corlewpsychology-example.com.au/

The client wants the site to be a one pager design (like the sites given above). Please include a section named “Our Specialisations”, and the next titled “What we treat”, then one titled “Our Team” Feel free to take inspiration from the included links for the layout of these parts of the site.

Please mock up a booking panel similar to the that appears when you click "book now" on https://www.quillbrookcare-example.com.au/# .

The client would prefer you use the current logo and colour green (in logo) for theming.

Current site: https://www.corlewpsychology-example.com.au/

The winning designers will be required to:
- Provide a secondary standard page template
- Provide a design for a flyout enquiry/booking form
- Supply all images used in the designs free of charge

```html
<!DOCTYPE html>
<html lang="en">
<head>
<meta charset="utf-8">
<title>Corlew &amp; Associates — Clinical Psychologists</title>
<link rel="stylesheet" href="https://fonts.googleapis.com/css2?family=Inter:wght@400;500;600;700&family=Playfair+Display:ital,wght@0,400;0,500;1,700;1,800&display=swap">
<style>
:root{
  --green:#6cc383;
  --green-dark:#4faa68;
  --ink:#1e1a45;
  --text:#3d3d4a;
  --muted:#6a6a75;
  --night:#1e1238;
  --paper:#f2f0ea;
  --white:#ffffff;
}
*{box-sizing:border-box;margin:0;padding:0}
html,body{width:1200px;height:3711px;overflow:hidden}
body{font-family:"Inter",sans-serif;color:var(--text);background:var(--white);position:relative}
.serif{font-family:"Playfair Display",serif}
.em{font-family:"Playfair Display",serif;font-style:italic;font-weight:800}
.eyebrow{font-size:13px;letter-spacing:3.5px;text-transform:uppercase;color:var(--ink);font-weight:500}
.heading{font-family:"Playfair Display",serif;font-weight:400;color:var(--ink);font-size:37px;line-height:41px}
.arrow{width:16px;height:12px;display:inline-block;vertical-align:middle}
section,header,footer{position:absolute;left:0;width:1200px}
.abs{position:absolute}

/* nav */
.site-nav{top:0;height:62px;background:var(--white);border-bottom:1px solid #eee}
.brand{left:109px;top:18px;font-weight:700;font-size:18px;color:var(--green);letter-spacing:-.3px;display:flex;align-items:center;gap:8px}
.brand-mark{width:12px;height:12px;background:var(--green)}
.nav-links{left:0;top:24px;width:1200px;height:16px;font-size:11.5px;color:#222}
.nav-links span{position:absolute;top:0;white-space:nowrap}
.nav-links .active{color:var(--green)}
.btn{display:inline-flex;align-items:center;gap:8px;border-radius:30px;font-size:12.5px;font-weight:500;white-space:nowrap}
.btn-book{left:976px;top:13px;width:114px;height:36px;justify-content:center;background:var(--green);color:#fff;font-size:12px}

/* hero */
.hero{top:62px;height:521px;background:linear-gradient(100deg,#3a3c3d 0%,#55534e 35%,#4a4743 60%,#2d2a28 100%)}
.hero-inner{position:absolute;inset:0;text-align:center;color:#fff}
.hero .eyebrow{position:absolute;top:164px;width:100%;color:#fff;font-size:12.5px}
.hero h1{position:absolute;top:188px;width:100%;font-family:"Playfair Display",serif;font-weight:400;font-size:52px;line-height:54px}
.hero h1 .em{color:var(--green)}
.btn-ghost{position:absolute;left:539px;top:321px;width:121px;height:36px;justify-content:center;border:1.5px solid #fff;color:#fff}

/* about */
.about{top:583px;height:555px;background:linear-gradient(90deg,#f2efe9 40%,#eef2ec 100%)}
.about .eyebrow{left:109px;top:95px}
.about .heading{left:109px;top:122px}
.about-intro{left:109px;top:220px;font-size:12px}
.checks{left:109px;top:246px;width:480px;list-style:none;font-size:11.5px;line-height:15px}
.checks li{display:flex;gap:8px;margin-bottom:10px}
.checks svg{flex:none;margin-top:1px}
.btn-outline{left:115px;top:424px;width:120px;height:35px;justify-content:center;border:1.5px solid var(--ink);color:var(--ink)}
.about-contact{left:256px;top:424px;border-left:1px solid #ccc;padding-left:16px;height:35px}
.about-contact small{display:block;font-family:"Playfair Display",serif;font-size:10px;color:var(--ink)}
.about-contact b{font-weight:400;font-size:13px;color:var(--ink)}
.about-photo{left:661px;top:64px;width:429px;height:426px;border-radius:26px;background:linear-gradient(160deg,#e7e2db 0%,#d9b23a 55%,#b4861d 100%)}

/* specialisations */
.specs{top:1138px;height:743px;background:var(--white);text-align:center}
.specs .eyebrow{position:absolute;top:60px;width:100%}
.specs .heading{position:absolute;top:92px;width:100%}
.card{position:absolute;width:230px;height:224px;border-radius:18px;border:1.5px solid;text-align:left;padding:30px 24px}
.card h3{font-family:"Playfair Display",serif;font-weight:400;font-size:15px;color:var(--ink)}
.card p{margin-top:18px;font-size:10.5px;line-height:15px;color:var(--muted)}
.card .more{position:absolute;left:24px;right:24px;bottom:26px;display:flex;justify-content:space-between;align-items:center;font-size:11px;font-weight:500;color:var(--ink)}
.c-mood{background:#e8fcef;border-color:#c2efcf}
.c-anx{background:linear-gradient(160deg,#4b4540,#2a2522);border-color:#2a2522}
.c-anx h3,.c-anx p,.c-anx .more{color:#fff}
.c-eat{background:#fde9ec;border-color:#f7cbd2}
.c-trauma{background:#eee9fd;border-color:#d4cbf5}
.c-phys{background:#fdf4e8;border-color:#f4dcbf}
.c-skills{background:#fdfde4;border-color:#eeefb5}
.c-family{background:#e8f9fc;border-color:#bfebf3}

/* treatments */
.treat{top:1881px;height:345px;background:linear-gradient(100deg,#e3f1f6 0%,#f2f4ee 50%,#f8f4e6 100%);overflow:hidden}
.treat .eyebrow{left:109px;top:80px}
.treat .heading{left:109px;top:106px}
.treat-text{left:109px;top:160px;width:240px;font-size:11px;line-height:15px}
.circle{width:36px;height:36px;border-radius:50%;background:#fff;display:flex;align-items:center;justify-content:center}
.treat-arrows{left:109px;top:236px;display:flex;gap:14px}
.t-card{position:absolute;top:62px;width:231px;height:220px;background:#fff;border-radius:6px;overflow:hidden}
.t-card .ph{height:162px}
.t-card span{display:block;padding:20px 19px;font-family:"Playfair Display",serif;font-size:15px;color:var(--ink);white-space:nowrap}

/* team */
.team{top:2226px;height:481px;background:var(--white);text-align:center}
.team .eyebrow{position:absolute;top:68px;width:100%}
.team .heading{position:absolute;top:97px;width:100%}
.m-card{position:absolute;top:166px;width:230px;height:253px;border-radius:12px;background:#f6f4f8;border:1px solid #ece8f0;padding:12px}
.m-card .ph{height:161px;border-radius:4px}
.m-card h4{margin-top:22px;font-family:"Playfair Display",serif;font-weight:400;font-size:15px;color:var(--ink)}
.m-card i{display:block;margin-top:6px;font-size:11px;color:var(--green)}
.team .circle{position:absolute;top:274px;border:1px solid #eee;box-shadow:0 2px 8px rgba(0,0,0,.08)}

/* blog */
.blog{top:2707px;height:547px;background:#efefe9;text-align:center}
.blog .eyebrow{position:absolute;top:66px;width:100%}
.blog .heading{position:absolute;top:97px;width:100%}
.b-card{position:absolute;top:161px;width:314px;height:322px;background:#fff;border-radius:12px;overflow:hidden;text-align:left}
.b-card .ph{height:163px}
.tag{position:absolute;top:154px;left:20px;background:#fff;border:1px solid var(--green);color:var(--green-dark);font-size:10px;padding:2px 8px;border-radius:10px}
.b-card h3{margin:31px 19px 0;font-family:"Playfair Display",serif;font-weight:500;font-size:15px;color:var(--ink)}
.b-card p{margin:12px 19px 0;font-size:11px;line-height:15px;color:var(--muted);height:46px;overflow:hidden}
.b-card .more{position:absolute;left:19px;right:19px;bottom:18px;border-top:1px solid #e5e5e5;padding-top:15px;display:flex;justify-content:space-between;font-size:11px;font-weight:500;color:var(--ink)}

/* cta + footer */
.footer{top:3254px;height:457px;background:linear-gradient(var(--white) 0 159px,var(--night) 159px)}
.cta{left:111px;top:62px;width:981px;height:193px;border-radius:26px;background:linear-gradient(90deg,#6ec586 0%,#7dcb90 55%,#8fd39d 100%);color:#fff}
.cta .eyebrow{position:absolute;left:43px;top:46px;color:#fff}
.cta h2{position:absolute;left:43px;top:68px;font-family:"Playfair Display",serif;font-weight:400;font-size:34px;line-height:39px}
.btn-light{position:absolute;left:816px;top:81px;width:119px;height:35px;justify-content:center;border:1.5px solid #fff;color:#fff}
.foot-nav{left:109px;top:288px;width:981px;display:flex;justify-content:space-between;font-size:12px;color:#fff;padding-bottom:18px;border-bottom:1px solid rgba(255,255,255,.15)}
.foot-nav span{flex:1;text-align:center;border-right:1px solid rgba(255,255,255,.3);white-space:nowrap}
.foot-nav span:last-child{border:0}
.foot-brand{left:109px;top:364px;font-weight:700;font-size:20px;color:var(--green);display:flex;align-items:center;gap:8px}
.foot-phone{left:498px;top:356px;display:flex;gap:10px;align-items:center;color:#fff}
.foot-phone .circle{width:38px;height:38px;background:var(--green)}
.foot-phone small{display:block;font-family:"Playfair Display",serif;font-size:10px}
.foot-phone b{font-weight:400;font-size:13px}
.copy{right:110px;top:371px;font-size:10.5px;color:#cfcbe0}
</style>
</head>
<body>

<header class="site-nav">
  <div class="abs brand"><span class="brand-mark"></span>Corlew &amp; Associates</div>
  <nav class="abs nav-links">
    <span class="active" style="left:405px">Home</span>
    <span style="left:462px">Common Conditions</span>
    <span style="left:597px">Specialist Clinics</span>
    <span style="left:714px">Kids</span>
    <span style="left:762px">About</span>
    <span style="left:820px">Resources</span>
    <span style="left:902px">Contact</span>
  </nav>
  <a class="abs btn btn-book">Book Now <svg class="arrow" viewBox="0 0 16 12"><path d="M1 6h13M9 1l5 5-5 5" fill="none" stroke="#fff" stroke-width="1.5"/></svg></a>
</header>

<section class="hero" role="img" aria-label="Photo of a young woman on a sofa talking with a psychologist in a warm consulting room">
  <div class="hero-inner">
    <p class="eyebrow">We specialise in many areas</p>
    <h1>Find the Right<br><span class="em">Psychologist</span> for You</h1>
    <a class="btn btn-ghost">Get Started <svg class="arrow" viewBox="0 0 16 12"><path d="M1 6h13M9 1l5 5-5 5" fill="none" stroke="#fff" stroke-width="1.5"/></svg></a>
  </div>
</section>

<section class="about">
  <p class="abs eyebrow">About us</p>
  <h2 class="abs heading">Resources for <span class="em">Health</span> Care<br>Professionals</h2>
  <p class="abs about-intro">We differ from other practices in several ways. At Corlew and Associates:</p>
  <ul class="abs checks">
    <li><svg width="13" height="13" viewBox="0 0 13 13"><circle cx="6.5" cy="6.5" r="6.5" fill="#6cc383"/><path d="M3.5 6.7l2 2 4-4" fill="none" stroke="#fff" stroke-width="1.5"/></svg>We are all clinical psychologists with post-graduate clinical training.</li>
    <li><svg width="13" height="13" viewBox="0 0 13 13"><circle cx="6.5" cy="6.5" r="6.5" fill="#6cc383"/><path d="M3.5 6.7l2 2 4-4" fill="none" stroke="#fff" stroke-width="1.5"/></svg>We have enough specialists in different conditions, so you will find the right psychologist to work with you.</li>
    <li><svg width="13" height="13" viewBox="0 0 13 13"><circle cx="6.5" cy="6.5" r="6.5" fill="#6cc383"/><path d="M3.5 6.7l2 2 4-4" fill="none" stroke="#fff" stroke-width="1.5"/></svg>Our clinicians are committed to staying up to date with research into the causes and treatments of common conditions.</li>
    <li><svg width="13" height="13" viewBox="0 0 13 13"><circle cx="6.5" cy="6.5" r="6.5" fill="#6cc383"/><path d="M3.5 6.7l2 2 4-4" fill="none" stroke="#fff" stroke-width="1.5"/></svg>We only use treatments that have a known basis of evidence showing them to be effective. We then adapt and tailor these treatments to each individual after a thorough assessment.</li>
  </ul>
  <a class="abs btn btn-outline">Learn More <svg class="arrow" viewBox="0 0 16 12"><path d="M1 6h13M9 1l5 5-5 5" fill="none" stroke="#1e1a45" stroke-width="1.5"/></svg></a>
  <div class="abs about-contact"><small>For All Appointments &amp; Enquiries</small><b>+61290004821</b></div>
  <div class="abs about-photo" role="img" aria-label="Photo of a psychologist and a young client talking on a mustard sofa"></div>
</section>

<section class="specs">
  <p class="eyebrow">Our Specialisations</p>
  <h2 class="heading">Tailored <span class="em">Therapy</span> for Every Stage<br>of Life and Mind</h2>

  <div class="card c-mood" style="left:109px;top:200px"><h3>Mood</h3><p>Coaching appt or consultation or free initial consultation ? Let me know your thoughts on, what if we add that they don't have to make any commitments.?</p><div class="more">Read More<svg class="arrow" viewBox="0 0 16 12"><path d="M1 6h13M9 1l5 5-5 5" fill="none" stroke="#1e1a45" stroke-width="1.5"/></svg></div></div>
  <div class="card c-anx" style="left:359px;top:200px" role="img" aria-label="Anxiety card over a dim photo of a person resting"><h3>Anxiety</h3><p>Coaching appt or consultation or free initial consultation ? Let me know your thoughts on, what if we add that they don't have to make any commitments.?</p><div class="more">Read More<svg class="arrow" viewBox="0 0 16 12"><path d="M1 6h13M9 1l5 5-5 5" fill="none" stroke="#fff" stroke-width="1.5"/></svg></div></div>
  <div class="card c-eat" style="left:609px;top:200px"><h3>Eating disorders</h3><p>Coaching appt or consultation or free initial consultation ? Let me know your thoughts on, what if we add that they don't have to make any commitments.?</p><div class="more">Read More<svg class="arrow" viewBox="0 0 16 12"><path d="M1 6h13M9 1l5 5-5 5" fill="none" stroke="#1e1a45" stroke-width="1.5"/></svg></div></div>
  <div class="card c-trauma" style="left:860px;top:200px"><h3>Trauma</h3><p>Coaching appt or consultation or free initial consultation ? Let me know your thoughts on, what if we add that they don't have to make any commitments.?</p><div class="more">Read More<svg class="arrow" viewBox="0 0 16 12"><path d="M1 6h13M9 1l5 5-5 5" fill="none" stroke="#1e1a45" stroke-width="1.5"/></svg></div></div>

  <div class="card c-phys" style="left:235px;top:455px"><h3>Physical Health</h3><p>Coaching appt or consultation or free initial consultation ? Let me know your thoughts on, what if we add that they don't have to make any commitments.?</p><div class="more">Read More<svg class="arrow" viewBox="0 0 16 12"><path d="M1 6h13M9 1l5 5-5 5" fill="none" stroke="#1e1a45" stroke-width="1.5"/></svg></div></div>
  <div class="card c-skills" style="left:485px;top:455px"><h3>Skills to EnhanceYour Life</h3><p>Coaching appt or consultation or free initial consultation ? Let me know your thoughts on, what if we add that they don't have to make any commitments.?</p><div class="more">Read More<svg class="arrow" viewBox="0 0 16 12"><path d="M1 6h13M9 1l5 5-5 5" fill="none" stroke="#1e1a45" stroke-width="1.5"/></svg></div></div>
  <div class="card c-family" style="left:735px;top:455px"><h3>Child and Family Services</h3><p>Coaching appt or consultation or free initial consultation ? Let me know your thoughts on, what if we add that they don't have to make any commitments.?</p><div class="more">Read More<svg class="arrow" viewBox="0 0 16 12"><path d="M1 6h13M9 1l5 5-5 5" fill="none" stroke="#1e1a45" stroke-width="1.5"/></svg></div></div>
</section>

<section class="treat">
  <p class="abs eyebrow">Treatments</p>
  <h2 class="abs heading">What We <span class="em">Treat</span></h2>
  <p class="abs treat-text">We have a specialised arm of the practice for kids, teens and families. Access our child and family clinic,&nbsp; PsychPlay4Kids, for issues relating to children and families.</p>
  <div class="abs treat-arrows">
    <span class="circle"><svg class="arrow" viewBox="0 0 16 12"><path d="M15 6H2M7 1L2 6l5 5" fill="none" stroke="#1e1a45" stroke-width="1.5"/></svg></span>
    <span class="circle"><svg class="arrow" viewBox="0 0 16 12"><path d="M1 6h13M9 1l5 5-5 5" fill="none" stroke="#1e1a45" stroke-width="1.5"/></svg></span>
  </div>
  <div class="t-card" style="left:377px"><div class="ph" role="img" aria-label="Photo of a frightened person covering their face" style="background:linear-gradient(150deg,#3a2a22,#6b3b1d 60%,#2b2220)"></div><span>Fears</span></div>
  <div class="t-card" style="left:628px"><div class="ph" role="img" aria-label="Photo of a young man sitting quietly on a sofa" style="background:linear-gradient(150deg,#e9e8e3,#9a9893 60%,#3c3c3c)"></div><span>Selective Mutism</span></div>
  <div class="t-card" style="left:878px"><div class="ph" role="img" aria-label="Photo of a stressed schoolboy at a classroom desk" style="background:linear-gradient(150deg,#d9cdb9,#3f5aa0 55%,#a39478)"></div><span>School Refusal</span></div>
  <div class="t-card" style="left:1128px"><div class="ph" role="img" aria-label="Photo relating to aggression" style="background:linear-gradient(150deg,#6a6350,#a49d8c)"></div><span>Aggression</span></div>
</section>

<section class="team">
  <p class="eyebrow">Therapists</p>
  <h2 class="heading">Meet Our <span class="em">Team</span></h2>
  <div class="m-card" style="left:109px"><div class="ph" role="img" aria-label="Portrait photo of therapist Mara Ellison" style="background:linear-gradient(150deg,#efeae6,#6b4f45 60%,#2a2120)"></div><h4>Mara Ellison</h4><i>Therapist</i></div>
  <div class="m-card" style="left:359px"><div class="ph" role="img" aria-label="Portrait photo of therapist Tavin Oruel" style="background:linear-gradient(150deg,#bdb8b0,#8a7461 55%,#26345a)"></div><h4>Tavin Oruel</h4><i>Therapist</i></div>
  <div class="m-card" style="left:609px"><div class="ph" role="img" aria-label="Portrait photo of therapist Dev Kalani" style="background:linear-gradient(150deg,#a9a7a0,#7a5d4b 55%,#2a2a2e)"></div><h4>Dev Kalani</h4><i>Therapist</i></div>
  <div class="m-card" style="left:860px"><div class="ph" role="img" aria-label="Portrait photo of therapist Lena Harwick" style="background:linear-gradient(150deg,#e7e3a0,#b38e76 50%,#4a3a33)"></div><h4>Lena Harwick</h4><i>Therapist</i></div>
  <span class="circle" style="left:90px;background:var(--green);border-color:var(--green)"><svg class="arrow" viewBox="0 0 16 12"><path d="M15 6H2M7 1L2 6l5 5" fill="none" stroke="#fff" stroke-width="1.5"/></svg></span>
  <span class="circle" style="left:1072px"><svg class="arrow" viewBox="0 0 16 12"><path d="M1 6h13M9 1l5 5-5 5" fill="none" stroke="#1e1a45" stroke-width="1.5"/></svg></span>
</section>

<section class="blog">
  <p class="eyebrow">Insights</p>
  <h2 class="heading">Latest <span class="em">Blog</span> Posts</h2>
  <article class="b-card" style="left:109px"><div class="ph" role="img" aria-label="Photo of two young women talking over a laptop" style="background:linear-gradient(150deg,#5a6a3e,#c89a6c 50%,#a35a2f)"></div><span class="tag">Cognitive Behavioural Therapy</span><h3>CBT for therapists</h3><p>This blog for CBT therapists contains weekly posts rich with clinical tips, therapy tools, solutions to common problems that arise...</p><div class="more">Read More<svg class="arrow" viewBox="0 0 16 12"><path d="M1 6h13M9 1l5 5-5 5" fill="none" stroke="#1e1a45" stroke-width="1.5"/></svg></div></article>
  <article class="b-card" style="left:443px"><div class="ph" role="img" aria-label="Photo of a woman wearing a face mask" style="background:linear-gradient(150deg,#e8e6e0,#6a5a50 55%,#2c2624)"></div><span class="tag">Online Therapy</span><h3>Online &amp; COVID</h3><p>Online Therapy -&nbsp; have your appointments conducted online. Psychological therapy can readily be adapted to the online medium. We...</p><div class="more">Read More<svg class="arrow" viewBox="0 0 16 12"><path d="M1 6h13M9 1l5 5-5 5" fill="none" stroke="#1e1a45" stroke-width="1.5"/></svg></div></article>
  <article class="b-card" style="left:776px"><div class="ph" role="img" aria-label="Photo of a therapist talking with a young girl in front of bookshelves" style="background:linear-gradient(150deg,#3a3634,#c9b8a6 50%,#8aa0c0)"></div><span class="tag">Kids, Teens And Familie</span><h3>Children</h3><p>We have a specialised arm of the practice for kids, teens and families. Access our child and family clinic...</p><div class="more">Read More<svg class="arrow" viewBox="0 0 16 12"><path d="M1 6h13M9 1l5 5-5 5" fill="none" stroke="#1e1a45" stroke-width="1.5"/></svg></div></article>
</section>

<footer class="footer">
  <div class="abs cta">
    <p class="eyebrow">Take the next step</p>
    <h2>Start on a Journey to the <span class="em">Best<br>Version</span> of Yourself</h2>
    <a class="btn btn-light">Contact Us <svg class="arrow" viewBox="0 0 16 12"><path d="M1 6h13M9 1l5 5-5 5" fill="none" stroke="#fff" stroke-width="1.5"/></svg></a>
  </div>
  <nav class="abs foot-nav"><span>Home</span><span>Common Conditions</span><span>Specialist Clinics</span><span>Kids</span><span>About</span><span>Resources</span><span>Contact</span></nav>
  <div class="abs foot-brand"><span class="brand-mark"></span>Corlew &amp; Associates</div>
  <div class="abs foot-phone">
    <span class="circle"><svg width="18" height="18" viewBox="0 0 24 24"><path d="M6.6 10.8a15 15 0 006.6 6.6l2.2-2.2a1 1 0 011-.25 11.4 11.4 0 003.6.57 1 1 0 011 1V20a1 1 0 01-1 1A17 17 0 013 4a1 1 0 011-1h3.5a1 1 0 011 1c0 1.25.2 2.45.57 3.57a1 1 0 01-.25 1z" fill="none" stroke="#fff" stroke-width="1.6"/></svg></span>
    <div><small>For All Appointments &amp; Enquiries</small><b>+61290004821</b></div>
  </div>
  <p class="abs copy">Copyright © 2013 – 2024 Corlew Psychology. All Rights Reserved.</p>
</footer>

</body>
</html>
```